Corvant Systems Business Card

Create an appealing and elegant Business card for corvant systems. Include logo and use related colors from website, be creative. Include Business name, my name, tile, address, contacts, address, and social media contacts if possible. Logo PSD file is attached.

Bleed Area: 3.46" x 2.32"
Trim: 3.3" x 2.16"
Safe Area: 3.14" x 2.02"

Save files as vector-based PDF with outlined text and PNG.
No crop marks
CMYK color setting

Business Card Info:

Corvant Systems

Dennis Halvorsen
Owner

512 Brindlemoor Rd Unit C
Harlow Falls, ME 02871
t. 1.888.555.0162
e. dennis.h@corvantsys.example
w. www.corvantsys.example

facebook. www.facebook.com/CorvantSys
twitter. twitter.com/corvantsys
pinterest. www.pinterest.com/corvantsys/

Target Market(s)

Business Owners and Partners

Industry/Entity Type

Business

Requirements
Must have
• Logo and related colors from website

```html
<!DOCTYPE html>
<html lang="en">
<head>
<meta charset="utf-8">
<title>Corvant Systems Business Card</title>
<link rel="stylesheet" href="https://fonts.googleapis.com/css2?family=Open+Sans:ital,wght@0,400;0,700;1,700&family=Arimo:wght@400;700&display=swap">
<style>
  :root {
    --blue: #4a6fa8;
    --blue-dark: #2c4a80;
    --blue-light: #8aa5cf;
    --ink: #1a1a1a;
    --grey: #555555;
    --paper: #ffffff;
    --stage: #e9ecf1;
  }
  * { margin: 0; padding: 0; box-sizing: border-box; }
  html, body { width: 1200px; height: 1200px; overflow: hidden; background: var(--stage); }
  .sheet {
    width: 1200px; height: 1200px;
    display: flex; flex-direction: column; align-items: center; justify-content: center; gap: 40px;
  }
  .card {
    position: relative; width: 820px; height: 537px; background: var(--paper);
    overflow: hidden; box-shadow: 0 6px 20px rgba(30, 45, 80, 0.18);
  }
  .card-art { position: absolute; inset: 0; width: 100%; height: 100%; }

  /* Front */
  .front-brand {
    position: absolute; left: 0; right: 0; top: 150px; text-align: center;
    font-family: "Open Sans", sans-serif; color: var(--ink); font-weight: 400; line-height: 1;
  }
  .front-brand .brand-top { font-size: 74px; letter-spacing: 3px; }
  .front-brand .brand-bottom { font-size: 74px; margin-top: 6px; }
  .front-url {
    position: absolute; left: 0; right: 0; top: 372px; text-align: center;
    font-family: "Open Sans", sans-serif; font-weight: 700; font-style: italic;
    font-size: 17px; color: var(--blue-dark); letter-spacing: 0.5px;
  }

  /* Back */
  .back-brand {
    position: absolute; left: 60px; top: 58px;
    font-family: "Open Sans", sans-serif; color: var(--ink); line-height: 1;
  }
  .back-brand .brand-top { font-size: 50px; letter-spacing: 2px; }
  .back-brand .brand-bottom { font-size: 50px; margin-top: 4px; }
  .person { position: absolute; left: 520px; top: 112px; font-family: "Arimo", sans-serif; }
  .person-name { font-size: 27px; font-weight: 700; color: var(--ink); }
  .person-title { font-size: 19px; font-weight: 700; color: var(--grey); margin-top: 4px; }
  .address {
    position: absolute; left: 80px; top: 250px; font-family: "Arimo", sans-serif;
    font-size: 22px; line-height: 1.4; color: var(--ink); font-style: normal;
  }
  .divider { position: absolute; left: 400px; top: 252px; width: 2px; height: 100px; background: var(--ink); }
  .contacts {
    position: absolute; left: 438px; top: 258px; list-style: none;
    font-family: "Arimo", sans-serif; font-size: 22px; color: var(--ink);
  }
  .contacts li { display: flex; align-items: center; gap: 12px; height: 31px; }
  .contacts svg { width: 20px; height: 20px; flex: none; }
  .social-band {
    position: absolute; left: 0; right: 0; bottom: 0; height: 165px;
    background: linear-gradient(120deg, var(--blue) 0%, var(--blue-light) 45%, var(--blue) 75%);
    display: flex; justify-content: space-around; align-items: center; padding: 0 30px 10px;
  }
  .social-band::after {
    content: ""; position: absolute; left: 0; right: 0; bottom: 0; height: 28px; background: var(--blue-dark);
  }
  .social { display: flex; flex-direction: column; align-items: center; gap: 10px; position: relative; z-index: 1; }
  .social-dot { width: 58px; height: 58px; border-radius: 50%; background: var(--paper); }
  .social-handle { font-family: "Arimo", sans-serif; font-weight: 700; font-size: 21px; color: var(--paper); }
</style>
</head>
<body>
<main class="sheet">

  <section class="card card-front" aria-label="Card front">
    <svg class="card-art" viewBox="0 0 820 537" aria-hidden="true">
      <path d="M0 0 H560 C380 10 170 50 0 190 Z" fill="#4a6fa8"/>
      <path d="M0 0 H380 C250 20 110 60 0 130 Z" fill="#8aa5cf" opacity="0.55"/>
      <path d="M820 150 C780 330 620 470 380 537 H820 Z" fill="#4a6fa8"/>
      <path d="M820 290 C770 400 690 480 600 537 H820 Z" fill="#8aa5cf" opacity="0.6"/>
    </svg>
    <div class="front-brand">
      <div class="brand-top">CORVANT</div>
      <div class="brand-bottom">Systems</div>
    </div>
    <div class="front-url">WWW.CORVANTSYS.EXAMPLE</div>
  </section>

  <section class="card card-back" aria-label="Card back">
    <svg class="card-art" viewBox="0 0 820 537" aria-hidden="true">
      <path d="M515 0 H735 L720 38 Q714 50 700 50 H550 Q536 50 530 38 Z" fill="#4a6fa8"/>
    </svg>
    <div class="back-brand">
      <div class="brand-top">CORVANT</div>
      <div class="brand-bottom">Systems</div>
    </div>
    <div class="person">
      <div class="person-name">Dennis Halvorsen</div>
      <div class="person-title">Owner</div>
    </div>
    <address class="address">512 Brindlemoor Rd Unit C<br>Harlow Falls,<br>ME 02871.</address>
    <div class="divider"></div>
    <ul class="contacts">
      <li>
        <svg viewBox="0 0 20 20"><path d="M3 7 Q10 1 17 7 L15 9 L12 7.5 L12 6 Q10 5 8 6 L8 7.5 L5 9 Z" fill="#1a1a1a"/><rect x="4" y="10" width="12" height="7" rx="1.5" fill="#1a1a1a"/><circle cx="10" cy="13.5" r="2" fill="#fff"/></svg>
        <span>1.888.555.0162</span>
      </li>
      <li>
        <svg viewBox="0 0 20 20"><rect x="2" y="5" width="16" height="11" fill="#1a1a1a"/><path d="M2.5 5.5 L10 11 L17.5 5.5" fill="none" stroke="#fff" stroke-width="1.4"/></svg>
        <span>dennis.h@corvantsys.example</span>
      </li>
      <li>
        <svg viewBox="0 0 20 20"><circle cx="10" cy="10" r="8" fill="none" stroke="#1a1a1a" stroke-width="1.6"/><ellipse cx="10" cy="10" rx="3.5" ry="8" fill="none" stroke="#1a1a1a" stroke-width="1.4"/><path d="M2 10 H18 M3.5 6 H16.5 M3.5 14 H16.5" stroke="#1a1a1a" stroke-width="1.2"/></svg>
        <span>www.corvantsys.example</span>
      </li>
    </ul>
    <div class="social-band">
      <div class="social"><span class="social-dot"></span><span class="social-handle">CorvantSys</span></div>
      <div class="social"><span class="social-dot"></span><span class="social-handle">CorvantSys</span></div>
      <div class="social"><span class="social-dot"></span><span class="social-handle">CorvantSys</span></div>
    </div>
  </section>

</main>
</body>
</html>
```